Flyer-Design für Seniorenbetreuung
Zielgruppe
Wir sind eine Genossenschaft, welche ihren Immobilienbestand gern erweitern möchte. Dafür soll für unsere Partnerfirma (welche im Seniorenbetreuungssektor tätig ist) eine Flyer erdacht werden, welcher Senioren bzw. ihre Angehörigen anspricht die Wohneigentum besitzen. Viele Senioren besitzen Ein-, Mehrfamilienhäuser oder Eigentumswohnungen und können oder wollen diese nicht weiter vererben. Zusätzlich sind sie durch die Kosten des Eigentums, wie Steuern oder Instandhaltungskosten belastet. Unsere Genossenschaft bietet eine Lösung des Problems. Eine Übernahme des Eigentums bei gleichzeitigem lebenslangem Wohnrecht. Die Zielgruppe soll in dem Flyer auf die bestehende Probleme angesprochen werden und gleichzeitig eine individuelle Lösung angeboten werden, welche eine Mitgliedschaft in dem sozialen Verbund der Genossenschaft ist.
Aufgabenstellung
Der Designer hat hier völlig freie Hand. Es sollte auf die Zielgruppe passen.
Passende Texte soll sich der Designer selbst erdenken.
Nachtrag: Ich habe mittlerweile viele Zuschriften bekommen, dass die Aufgabenstellung sich Texte auszudenken etwas zu allgemein gefasst ist, daher versuche ich hier nochmal etwas Licht in Dunkle zu bringen. Ich habe genauso wenig eine Idee, wie und mit welcher Wortwahl ein Senior auf einfühlsame Weise darauf angesprochen werden soll, ob er nicht sein Haus verkaufen möchte. Meine bisherigen Ideen waren:
'Haben sie schon einmal über den Verkauf ihrer Immobilie nachgedacht? Wussten sie, dass sie ihr Wohneigentum im vollen Umfang weiter nutzen können, ohne weiter die Kosten tragen zu müssen? Sie wollen wissen wie? Rufen sie doch einfach an und ich werde ihnen genau erklären, welche Vorzüge die Mitgliedschaft in einer Genossenschaft mit sich bringt.'
Allerdings erscheint mir das viel zu direkt und ich finde nicht die richtigen Worte diese Personengruppe in dem Maße anzusprechen, wie es nötig wäre, um sie zu einem Anruf zu bewegen. Daher hatte ich gehofft, dass sie hier ein findiger Designer findet, welcher eine bessere kreative Art hat als ich.
Vielleicht ist es die falsche Plattform, vielleicht schaffen wir es nicht die Vorgaben zu spezifizieren. Bilder anzuordnen ist sicher sehr wichtig, auch ist es wichtig aufhellende Elemente einzubringen. Aber wir suchen jemanden der einen Flyer so gestalten kann das der Flyer etwas ausdrückt, das eine Botschaft vermittelt wird, das auf einem Blick der Senior den Wunsch verspürt, bei uns anzurufen. Das heißt viel wichtiger als Bilder, ist der Inhalt der Ansprache. Nicht unbedingt der Inhalt, sondern das WIE. Nochmal: wir wollen ältere Menschen dazu bewegen ihr Eigentum auf Grund von Reperaturrückstau, Überlastung, gesundheitlichen Einschränkungen, finanziellen Schwierigkeiten, zu großem Aufwand in eine Genossenschaft einzubringen. Ds heißt S..

```html
<!DOCTYPE html>
<html lang="de">
<head>
<meta charset="utf-8">
<title>Ohne Sorgen leben – Flyer</title>
<link href="https://fonts.googleapis.com/css2?family=Montserrat:ital,wght@0,600;0,700;1,600&display=swap" rel="stylesheet">
<style>
  :root {
    --page-bg: #e4e4e4;
    --paper: #ffffff;
    --orange: #f5a50a;
    --orange-deep: #eb9a00;
    --orange-light: #fde3b0;
    --navy: #1e4660;
    --green: #2f5a3a;
    --white: #ffffff;
  }
  * { margin: 0; padding: 0; box-sizing: border-box; }
  html, body {
    width: 1190px; height: 1200px; overflow: hidden;
    background: var(--page-bg);
    font-family: "Montserrat", Arial, sans-serif;
  }
  .flyer {
    position: absolute; left: 388px; top: 16px;
    width: 413px; height: 1167px;
    background: var(--paper);
    overflow: hidden;
    box-shadow: 0 2px 10px rgba(0,0,0,.08);
  }
  .flyer-header {
    position: absolute; left: 0; top: 0; width: 100%; height: 81px;
    display: flex; align-items: center; justify-content: center; gap: 44px;
    background: var(--paper);
    box-shadow: 0 3px 8px rgba(0,0,0,.12);
    z-index: 2;
  }
  .brand { display: flex; align-items: center; gap: 6px; font-weight: 700; font-size: 11px; line-height: 1.15; }
  .brand-dot { width: 22px; height: 22px; border-radius: 50%; flex: none; }
  .brand--coop { color: var(--green); }
  .brand--coop .brand-dot { background: var(--green); }
  .brand--care { color: var(--orange-deep); }
  .brand--care .brand-dot { background: var(--orange-deep); }

  .hero-photo {
    position: absolute; left: 0; top: 81px; width: 100%; height: 302px;
    background: linear-gradient(160deg, #e9e6e2 0%, #b9b4ac 40%, #6f7782 70%, #3e5878 100%);
  }
  .hero-label {
    position: absolute; left: 0; top: 330px; width: 301px; height: 55px;
    background: var(--orange);
    color: var(--white);
    font-weight: 600; font-size: 22.5px; letter-spacing: .6px;
    display: flex; align-items: center; padding-left: 12px;
    z-index: 1;
  }
  .question {
    position: absolute; left: 48px; width: 320px;
    color: var(--navy);
    font-weight: 700; font-size: 16.6px; line-height: 21.6px; letter-spacing: .2px;
  }
  .question--sale { top: 469px; }
  .question--use { top: 578px; }
  .marker {
    position: absolute; left: 0; width: 33px; height: 3px;
    background: var(--orange);
  }
  .marker--sale { top: 510px; }
  .marker--use { top: 627px; }
  .answer {
    position: absolute; left: 48px; top: 672px; width: 330px;
    color: var(--orange);
    font-style: italic; font-weight: 600; font-size: 19.4px; line-height: 25px;
  }
  .contact-panel {
    position: absolute; left: 0; top: 786px; width: 100%; height: 381px;
  }
  .contact-panel svg { display: block; }
  .contact-text {
    position: absolute; left: 34px; top: 1000px;
    color: var(--white); font-weight: 700;
  }
  .contact-title { font-size: 24px; letter-spacing: .3px; margin-bottom: 14px; }
  .contact-line { font-size: 19.5px; line-height: 25px; letter-spacing: .4px; }
  .contact-line--invite { margin-bottom: 6px; }
</style>
</head>
<body>
  <main class="flyer">
    <header class="flyer-header">
      <div class="brand brand--coop"><span class="brand-dot"></span><span>Wohnhafen eG</span></div>
      <div class="brand brand--care"><span class="brand-dot"></span><span>Lebensbogen Betreuung</span></div>
    </header>

    <div class="hero-photo" role="img" aria-label="Foto: älteres Paar sitzt entspannt zusammen auf einem Sofa im hellen Wohnzimmer"></div>
    <h1 class="hero-label">OHNE SORGEN LEBEN</h1>

    <span class="marker marker--sale"></span>
    <p class="question question--sale">Haben sie schon einmal über den Verkauf ihrer Immobilie nachgedacht?</p>

    <span class="marker marker--use"></span>
    <p class="question question--use">Sie möchten Ihr Wohneigentum im vollen Umfang weiter nutzen können, ohne weiter die Kosten tragen zu müssen?</p>

    <p class="answer">Dann werden Sie Mitglied in dem sozialen Verbund der Genossenschaft!</p>

    <div class="contact-panel">
      <svg width="413" height="381" viewBox="0 0 413 381" role="img" aria-label="Orangefarbene Fläche mit blassem Foto einer Betreuerin und eines Seniors am Tisch">
        <defs>
          <linearGradient id="panelTone" x1="0" y1="0" x2="1" y2="1">
            <stop offset="0" stop-color="#f7ad1c"/>
            <stop offset="0.55" stop-color="#f2a40e"/>
            <stop offset="1" stop-color="#eda013"/>
          </linearGradient>
        </defs>
        <path d="M0 12 C 70 -6, 150 6, 230 26 S 360 42, 413 30 L 413 381 L 0 381 Z" fill="var(--orange-light)"/>
        <path d="M0 26 C 70 8, 150 20, 230 40 S 360 56, 413 44 L 413 381 L 0 381 Z" fill="url(#panelTone)"/>
      </svg>
    </div>

    <div class="contact-text">
      <p class="contact-title">Wir beraten Sie gerne!</p>
      <p class="contact-line contact-line--invite">Kontaktieren Sie uns unter:</p>
      <p class="contact-line">01234 - 567 890 12</p>
      <p class="contact-line">www.wohnhafen-beispiel.de</p>
    </div>
  </main>
</body>
</html>
```